Qvo Brightforge Website

All the descriptions are available in the attached file. The designer has to structure the website and find the right images and icons. The website should look modern and avoid using images of real humans rather use animated images. Please note that the design should include home page, all the 4 services page , the contact us would be at the bottom of home page.

```html
<!DOCTYPE html>
<html lang="en">
<head>
<meta charset="utf-8">
<title>Qvo Brightforge</title>
<link href="https://fonts.googleapis.com/css2?family=Montserrat:wght@400;500;600;700;800&display=swap" rel="stylesheet">
<style>
:root{
  --blue:#0a6fdc;
  --blue-deep:#0558b8;
  --orange:#f7850f;
  --green:#47b51d;
  --ink:#1b1b1b;
  --muted:#555;
  --grey-bg:#f4f4f4;
  --pill:#e6e6e6;
  --dark:#2b2d31;
  --white:#fff;
}
*{margin:0;padding:0;box-sizing:border-box}
html,body{width:1200px;height:4199px;overflow:hidden}
body{position:relative;font-family:"Montserrat",sans-serif;color:var(--ink);background:var(--white)}
.abs{position:absolute}
.pill{position:absolute;display:flex;align-items:center;justify-content:center;border-radius:30px;font-size:13px;font-weight:500;letter-spacing:.5px;text-transform:uppercase;color:#444;background:var(--pill);box-shadow:0 3px 0 #bdbdbd inset, 0 0 0 2px #fff inset;border:1px solid #cfcfcf}
.pill.orange{background:var(--orange);color:#fff;border-color:#fff;box-shadow:0 0 0 2px var(--orange)}
.pill.light{background:#fff;border:2px solid #ddd;box-shadow:0 2px 0 #aaa}

/* hero */
.hero-photo{left:0;top:0;width:1200px;height:600px;background:linear-gradient(100deg,#8f8a84 0%,#c9c4bd 30%,#e9e6e2 55%,#b8a89a 75%,#6f6259 100%)}
.logo{font-weight:800;font-size:24px;color:var(--blue);display:flex;align-items:center;gap:8px;line-height:1}
.logo .dot{width:12px;height:12px;background:var(--orange)}
.nav{left:540px;top:47px;display:flex;gap:30px;font-size:13px;font-weight:600;letter-spacing:1px;color:#fff}
.nav .active{color:var(--orange);text-decoration:underline}
.nav-icon{top:38px;width:36px;height:36px;border-radius:50%;display:flex;align-items:center;justify-content:center}
.hero-kicker{left:0;width:1200px;top:242px;text-align:center;color:var(--orange);font-size:15px;font-weight:700;letter-spacing:1px}
.hero-title{left:0;width:1200px;top:262px;text-align:center;color:var(--blue);font-size:50px;font-weight:800;letter-spacing:1px}

/* welcome */
.section-kicker{left:0;width:1200px;text-align:center;color:var(--blue);font-size:16px;font-weight:700}
.section-title{left:0;width:1200px;text-align:center;color:var(--blue);font-size:32px;font-weight:700;letter-spacing:1px}
.underline{height:3px;background:var(--orange);left:555px;width:90px}
.welcome-text{left:215px;width:770px;top:762px;text-align:center;font-size:13.5px;line-height:21px;color:#222}
.sq{position:absolute}

/* services */
.services-band{left:0;top:968px;width:1200px;height:1450px;background:var(--blue)}
.services-title{left:0;width:1200px;top:1044px;text-align:center;color:var(--orange);font-size:33px;font-weight:800;letter-spacing:1px}
.card-frame{width:455px;height:276px;border:2px solid var(--orange);border-radius:20px 110px 20px 20px;border-left:none;border-bottom:none}
.card{width:455px;height:278px;background:#fff;border-radius:20px 110px 20px 20px;padding:34px 70px}
.art{width:100%;height:100%;border-radius:60px 60px 30px 30px}
.svc-title{color:#fff;font-size:27px;font-weight:700;letter-spacing:1px}
.svc-text{color:#cfe2fb;font-size:13.5px;line-height:21px;width:430px}
.right{text-align:right}

/* cta */
.cta-text{left:190px;top:2588px;font-size:31px;line-height:41px;color:#333}
.cta-text b{color:var(--blue);font-weight:800}

/* blog */
.blog-band{left:0;top:2775px;width:1200px;height:460px;background:var(--grey-bg)}
.blog-card{width:324px;height:190px;background:#fff;top:2930px}
.blog-date{position:absolute;left:22px;top:28px;text-align:center;color:var(--blue);font-size:30px;font-weight:700;line-height:1}
.blog-date small{display:block;font-size:11px;font-weight:400;color:#666;margin-top:4px}
.blog-head{position:absolute;left:97px;top:28px;width:210px;color:var(--blue);font-size:14px;font-weight:600;line-height:18px}
.blog-body{position:absolute;left:97px;top:78px;width:210px;color:#555;font-size:12.5px;line-height:19px}

/* form */
.field{position:absolute;border:1px solid #d5d5d5;border-radius:20px;background:#fff;font-size:12.5px;color:#aaa;display:flex;align-items:center;gap:10px;padding-left:16px}
.field.area{align-items:flex-start;padding-top:14px;border-radius:16px}
.submit{background:#5b5b5b;color:#fff;border-color:#fff;box-shadow:0 0 0 2px #5b5b5b}

/* footer */
.footer-bg{left:0;top:3850px;width:1200px;height:349px;background:linear-gradient(180deg,#3a3b3f,#2b2d31)}
.contact-bar{left:108px;top:3998px;width:984px;height:84px;background:#fff;border-radius:4px;display:flex;align-items:center;padding:0 30px;font-size:13px;color:#111;line-height:19px}
.contact-item{display:flex;align-items:center;gap:14px}
.social{width:14px;height:14px;border-radius:50%;border:1.5px solid #999}
.foot-nav{left:0;width:1200px;top:4117px;display:flex;justify-content:center;gap:38px;color:#fff;font-size:13px;font-weight:600;letter-spacing:1px}
.copyright{left:0;width:1200px;top:4146px;text-align:center;color:#fff;font-size:12.5px}
</style>
</head>
<body>

<!-- HERO -->
<div class="abs hero-photo" role="img" aria-label="Photo of a smiling consultant with a colleague working at a laptop in a bright office"></div>
<svg class="abs" style="left:0;top:430px" width="1200" height="180" viewBox="0 0 1200 180">
  <path d="M0 40 C150 0 300 60 420 110 C540 160 650 170 760 130 C900 80 1050 30 1200 100 L1200 180 L0 180Z" fill="#fff"/>
  <path d="M0 40 C150 0 300 60 420 110 C300 80 150 40 0 60Z" fill="var(--blue)"/>
  <path d="M760 130 C900 80 1050 30 1200 100 L1200 120 C1060 60 900 90 760 130Z" fill="var(--blue)"/>
</svg>

<div class="abs logo" style="left:88px;top:40px"><span class="dot"></span>Qvo Brightforge</div>
<nav class="abs nav">
  <span class="active">HOME</span><span>SERVICES</span><span>PRODUCTS</span><span>BLOG</span><span>CONTACT US</span>
</nav>
<div class="abs nav-icon" style="left:1030px;background:#555">
  <svg width="16" height="16" viewBox="0 0 24 24"><path d="M6 3l4 4-2 3c1 2 4 5 6 6l3-2 4 4-3 3C10 21 3 14 3 6z" fill="none" stroke="#fff" stroke-width="1.8"/></svg>
</div>
<div class="abs nav-icon" style="left:1075px;background:var(--orange)">
  <svg width="16" height="16" viewBox="0 0 24 24"><rect x="3" y="5" width="18" height="14" rx="1" fill="none" stroke="#fff" stroke-width="1.8"/><path d="M3 6l9 7 9-7" fill="none" stroke="#fff" stroke-width="1.8"/></svg>
</div>
<div class="abs hero-kicker">ADVANCING INNOVATION THROUGH</div>
<div class="abs hero-title">IT CONSULTING</div>
<div class="pill orange" style="left:523px;top:341px;width:153px;height:32px">Consult Now</div>

<!-- WELCOME -->
<div class="abs section-kicker" style="top:668px">WELCOME TO</div>
<div class="abs section-title" style="top:688px">QVO BRIGHTFORGE</div>
<div class="abs underline" style="top:734px"></div>
<p class="abs welcome-text">We are a forward-thinking IT consulting firm specializing in providing cutting-edge data analytics, web application development, and mobile app development services. Our passion for innovation and technology drives us to deliver tailor-made solutions that empower businesses to thrive in the digital landscape.</p>
<div class="pill" style="left:526px;top:854px;width:148px;height:32px">Read More</div>
<div class="sq" style="left:1034px;top:838px;width:30px;height:30px;background:var(--green)"></div>
<div class="sq" style="left:1064px;top:868px;width:48px;height:46px;background:var(--orange)"></div>

<!-- SERVICES -->
<div class="abs services-band"></div>
<div class="sq" style="left:1000px;top:928px;width:64px;height:62px;background:var(--blue);border:4px solid #fff"></div>
<div class="abs services-title">SERVICES</div>

<div class="abs card-frame" style="left:96px;top:1117px"></div>
<div class="abs card" style="left:88px;top:1124px"><div class="art" role="img" aria-label="Illustration of two people presenting analytics charts on a large dashboard" style="background:linear-gradient(160deg,#2fb58a,#e6ecfb 55%,#d9defa)"></div></div>
<div class="abs svc-title" style="left:614px;top:1178px">DATA ANALYTICS</div>
<p class="abs svc-text" style="left:614px;top:1222px">Lorem Ipsum is simply dummy text of the printing and typesetting industry. Lorem Ipsum has been the industry's standard dummy text ever since the...</p>
<div class="pill light" style="left:614px;top:1306px;width:152px;height:34px">Read More</div>

<div class="abs card-frame" style="left:658px;top:1417px"></div>
<div class="abs card" style="left:650px;top:1424px"><div class="art" role="img" aria-label="Illustration of developers working at desks with screens of code and web layouts" style="background:linear-gradient(160deg,#f0f3fb,#dfe6f7 50%,#f7f3ea)"></div></div>
<div class="abs svc-title right" style="left:156px;width:430px;top:1486px">WEB DEVELOPMENT</div>
<p class="abs svc-text right" style="left:156px;top:1530px">Lorem Ipsum is simply dummy text of the printing and typesetting industry. Lorem Ipsum has been the industry's standard dummy text ever since the...</p>
<div class="pill light" style="left:434px;top:1614px;width:152px;height:34px">Read More</div>

<div class="abs card-frame" style="left:96px;top:1716px"></div>
<div class="abs card" style="left:88px;top:1723px"><div class="art" role="img" aria-label="Illustration of two people building a mobile app interface on a large phone" style="background:linear-gradient(160deg,#fbe9dd,#f4f1ee 50%,#e4ecfb)"></div></div>
<div class="abs svc-title" style="left:614px;top:1778px">MOBILE APP DEVELOPMENT</div>
<p class="abs svc-text" style="left:614px;top:1822px">Lorem Ipsum is simply dummy text of the printing and typesetting industry. Lorem Ipsum has been the industry's standard dummy text ever since the...</p>
<div class="pill orange" style="left:616px;top:1907px;width:148px;height:32px">Read More</div>

<div class="abs card-frame" style="left:658px;top:2017px"></div>
<div class="abs card" style="left:650px;top:2024px"><div class="art" role="img" aria-label="Illustration of two people launching a rocket as a start-up partnership" style="background:linear-gradient(160deg,#f6f8fd,#e3ebfa 50%,#fdeede)"></div></div>
<div class="abs svc-title right" style="left:156px;width:430px;top:2078px">START-UP PARTNER</div>
<p class="abs svc-text right" style="left:156px;top:2122px">Lorem Ipsum is simply dummy text of the printing and typesetting industry. Lorem Ipsum has been the industry's standard dummy text ever since the...</p>
<div class="pill light" style="left:434px;top:2206px;width:152px;height:34px">Read More</div>

<svg class="abs" style="left:0;top:2350px" width="1200" height="160" viewBox="0 0 1200 160">
  <path d="M0 40 C200 -10 350 60 550 70 C800 80 1000 10 1200 0 L1200 140 C1000 100 800 80 600 110 C400 140 200 60 0 30Z" fill="#5f6166"/>
  <path d="M0 60 C200 20 350 80 560 80 C800 80 1000 30 1200 50 L1200 60 C1000 110 850 110 650 130 C450 150 300 120 200 90 C120 70 60 60 0 80Z" fill="var(--blue)"/>
  <path d="M0 80 C60 60 120 70 200 90 C300 120 450 150 650 130 C850 110 1000 110 1200 60 L1200 160 L0 160Z" fill="#fff"/>
  <path d="M0 0 L1200 0 L1200 50 C1000 30 800 80 560 80 C350 80 200 20 0 60Z" fill="var(--blue)"/>
</svg>

<!-- CTA -->
<div class="abs cta-text">Looking to build <b>SOFTWARE</b><br><b>PRODUCTS</b> for industry of your choice!</div>
<div class="pill light" style="left:842px;top:2611px;width:166px;height:34px">Consult Now</div>

<!-- BLOG -->
<div class="abs blog-band"></div>
<div class="sq" style="left:82px;top:2644px;width:30px;height:30px;background:var(--green)"></div>
<div class="sq" style="left:112px;top:2674px;width:48px;height:46px;background:var(--orange)"></div>
<div class="sq" style="left:54px;top:2738px;width:56px;height:56px;background:var(--blue)"></div>
<div class="abs section-title" style="top:2848px">BLOG</div>
<div class="abs" style="left:558px;top:2890px;width:84px;height:2px;background:var(--blue)"></div>

<div class="abs blog-card" style="left:88px">
  <div class="blog-date">12<small>May, 23</small></div>
  <div class="blog-head">Lorem Ipsum is simply dummy text of the printing</div>
  <div class="blog-body">Lorem Ipsum has been the industry's standard dummy...</div>
  <div class="pill" style="left:97px;top:128px;width:122px;height:24px;font-size:11px">Read More</div>
</div>
<div class="abs blog-card" style="left:438px">
  <div class="blog-date">10<small>May, 23</small></div>
  <div class="blog-head">Lorem Ipsum is simply dummy text of the printing</div>
  <div class="blog-body">Lorem Ipsum has been the industry's standard dummy...</div>
  <div class="pill" style="left:97px;top:128px;width:122px;height:24px;font-size:11px">Read More</div>
</div>
<div class="abs blog-card" style="left:788px">
  <div class="blog-date">09<small>May, 23</small></div>
  <div class="blog-head">Lorem Ipsum is simply dummy text of the printing</div>
  <div class="blog-body">Lorem Ipsum has been the industry's standard dummy...</div>
  <div class="pill orange" style="left:97px;top:128px;width:122px;height:24px;font-size:11px">Read More</div>
</div>
<div class="pill" style="left:535px;top:3164px;width:130px;height:32px">View All</div>

<svg class="abs" style="left:0;top:3170px" width="1200" height="140" viewBox="0 0 1200 140">
  <path d="M0 0 L1200 0 L1200 40 C1050 50 900 100 700 105 C500 110 300 60 0 50Z" fill="var(--grey-bg)"/>
  <path d="M0 50 C300 60 500 110 700 105 C900 100 1050 50 1200 40 L1200 60 C1000 80 900 140 650 140 C450 140 300 50 150 30 C90 25 40 30 0 40Z" fill="var(--blue)"/>
  <path d="M0 40 C40 30 90 25 150 30 C300 50 450 140 650 140 C900 140 1000 80 1200 60 L1200 140 L0 140Z" fill="#fff" opacity="0"/>
</svg>

<!-- CONTACT FORM -->
<div class="abs section-title" style="top:3370px">GET IN TOUCH</div>
<div class="abs" style="left:558px;top:3410px;width:84px;height:2px;background:var(--blue)"></div>

<div class="field" style="left:302px;top:3453px;width:290px;height:38px">
  <svg width="12" height="12" viewBox="0 0 24 24"><circle cx="12" cy="8" r="4" fill="none" stroke="var(--blue)" stroke-width="2"/><path d="M4 21c0-5 16-5 16 0" fill="none" stroke="var(--blue)" stroke-width="2"/></svg>First Name</div>
<div class="field" style="left:608px;top:3453px;width:290px;height:38px">
  <svg width="12" height="12" viewBox="0 0 24 24"><circle cx="12" cy="8" r="4" fill="none" stroke="var(--blue)" stroke-width="2"/><path d="M4 21c0-5 16-5 16 0" fill="none" stroke="var(--blue)" stroke-width="2"/></svg>Last Name</div>
<div class="field" style="left:302px;top:3503px;width:290px;height:38px">
  <svg width="12" height="12" viewBox="0 0 24 24"><rect x="3" y="5" width="18" height="14" fill="none" stroke="var(--blue)" stroke-width="2"/><path d="M3 6l9 7 9-7" fill="none" stroke="var(--blue)" stroke-width="2"/></svg>Email</div>
<div class="field" style="left:608px;top:3503px;width:290px;height:38px">
  <svg width="12" height="12" viewBox="0 0 24 24"><rect x="7" y="2" width="10" height="20" rx="2" fill="none" stroke="var(--blue)" stroke-width="2"/></svg>Phone</div>
<div class="field area" style="left:302px;top:3555px;width:596px;height:96px">
  <svg width="12" height="12" viewBox="0 0 24 24"><rect x="3" y="3" width="18" height="18" fill="none" stroke="var(--blue)" stroke-width="2"/></svg>How can we help?</div>
<div class="pill submit" style="left:541px;top:3683px;width:118px;height:32px">Submit</div>

<!-- FOOTER -->
<div class="abs footer-bg" role="img" aria-label="Faded office photo behind the footer"></div>
<svg class="abs" style="left:0;top:3780px" width="1200" height="110" viewBox="0 0 1200 110">
  <path d="M0 0 L1200 0 L1200 20 C1000 70 800 90 600 80 C400 70 200 20 0 40Z" fill="#fff"/>
  <path d="M0 40 C200 20 400 70 600 80 C800 90 1000 70 1200 20 L1200 40 C1000 110 800 110 600 100 C380 90 200 60 0 70Z" fill="var(--blue)"/>
</svg>
<div class="sq" style="left:1034px;top:3760px;width:30px;height:30px;background:var(--green)"></div>
<div class="sq" style="left:1064px;top:3790px;width:48px;height:46px;background:var(--orange)"></div>
<div class="sq" style="left:1000px;top:3850px;width:64px;height:62px;background:var(--blue);border:4px solid #fff"></div>

<div class="abs logo" style="left:0;width:1200px;justify-content:center;top:3918px;font-size:30px;color:#fff"><span class="dot"></span>Qvo Brightforge</div>

<div class="abs contact-bar">
  <div class="contact-item" style="width:255px">
    <svg width="18" height="22" viewBox="0 0 24 30"><path d="M12 1C6 1 2 5 2 11c0 7 10 18 10 18s10-11 10-18C22 5 18 1 12 1z" fill="var(--blue)"/><circle cx="12" cy="11" r="4" fill="#fff"/></svg>
    <span>Suite 12/40 Harlow Lane,<br>Eastmere WA 6020</span></div>
  <div class="contact-item" style="width:260px">
    <svg width="22" height="16" viewBox="0 0 24 18"><rect x="1" y="1" width="22" height="16" fill="var(--blue)"/><path d="M1 1l11 9 11-9" fill="none" stroke="#fff" stroke-width="2"/></svg>
    <span>hello@qvobrightforge.example</span></div>
  <div class="contact-item" style="width:230px">
    <svg width="18" height="18" viewBox="0 0 24 24"><path d="M6 2l5 5-3 3c1 2 4 5 6 6l3-3 5 5-3 4C10 22 2 14 2 5z" fill="var(--blue)"/></svg>
    <span>(Sales / Support)<br>+61 (08) 5550 1234</span></div>
  <div style="display:flex;gap:18px;align-items:center;margin-left:auto">
    <span class="social"></span><span class="social"></span>
    <span style="width:26px;height:26px;border-radius:50%;background:var(--orange)"></span>
    <span class="social"></span>
  </div>
</div>

<nav class="abs foot-nav">
  <span style="color:var(--orange);text-decoration:underline">HOME</span><span>SERVICES</span><span>PRODUCTS</span><span>BLOG</span><span>CONTACT US</span>
</nav>
<div class="abs copyright">Copyright © 2023 Qvo Brightforge. All Rights Reserved</div>
<div class="abs" style="left:1120px;top:4116px;width:28px;height:28px;border-radius:50%;border:1.5px solid #777"></div>

</body>
</html>
```